Property developer, money partner needs business card design using logo concept provided

Our company develops residential properties, does money lends for joint ventures in property deals and finds property deals for other money partners. We have provided a basic logo for you to work from. Any graphic or logo design on the card is to communicate development and finance collaboration. Color choice is not so important for us, but color choice does need to reflect professionalism.

```html
<!DOCTYPE html>
<html lang="en">
<head>
<meta charset="utf-8">
<title>Keystone Property Partners – Business Card</title>
<link href="https://fonts.googleapis.com/css2?family=Poppins:wght@400;500;600&display=swap" rel="stylesheet">
<style>
  :root {
    --canvas: #ececec;
    --card: #ffffff;
    --shadow: #a9a9a9;
    --brand-red: #990000;
    --brand-blue: #0565aa;
    --brand-navy: #06408a;
    --ink: #000000;
    --line-red: #b23a3a;
  }
  * { margin: 0; padding: 0; box-sizing: border-box; }
  html, body { width: 1200px; height: 1200px; overflow: hidden; background: var(--canvas); font-family: "Poppins", sans-serif; color: var(--ink); }
  .stage { position: relative; width: 1200px; height: 1200px; }
  .card-shadow { position: absolute; background: var(--shadow); filter: blur(3px); }
  .card { position: absolute; left: 181px; width: 838px; height: 479px; background: var(--card); overflow: hidden; }
  .card--front { top: 110px; }
  .card--back { top: 611px; }
  .band { position: absolute; }
  .wordmark { position: absolute; text-align: center; white-space: nowrap; }
  .wordmark__name { font-weight: 600; letter-spacing: 0.3em; line-height: 1; color: var(--ink); }
  .wordmark__tagline { font-weight: 400; line-height: 1; color: var(--ink); }
  .wordmark__acn { font-weight: 500; line-height: 1; color: var(--ink); }
  .brand-dot { position: absolute; border-radius: 50%; background: linear-gradient(135deg, var(--brand-blue), var(--brand-navy)); }

  .front .brand-dot { left: 188px; top: 177px; width: 124px; height: 124px; }
  .front .wordmark { left: 336px; top: 198px; width: 320px; }
  .front .wordmark__name { font-size: 38px; margin-right: -0.3em; }
  .front .wordmark__tagline { font-size: 23px; letter-spacing: 0.2em; margin-top: 10px; }
  .front .wordmark__acn { font-size: 14px; letter-spacing: 0.3em; margin-top: 9px; }

  .back .brand-dot { left: 527px; top: 96px; width: 152px; height: 152px; }
  .back .wordmark { left: 493px; top: 322px; width: 220px; }
  .back .wordmark__name { font-size: 25px; margin-right: -0.3em; }
  .back .wordmark__tagline { font-size: 16px; letter-spacing: 0.2em; margin-top: 5px; }
  .back .wordmark__acn { font-size: 10px; letter-spacing: 0.3em; margin-top: 5px; }

  .name-tab { position: absolute; left: 0; top: 98px; width: 81px; height: 70px; background: var(--brand-red); border-radius: 0 5px 5px 0; }
  .name-tab__stem { position: absolute; left: 0; top: 0; width: 32px; height: 100px; background: var(--brand-red); }
  .name-tab svg { position: absolute; left: 27px; top: 19px; }
  .holder { position: absolute; left: 95px; top: 96px; }
  .holder__name { font-size: 46px; font-weight: 600; line-height: 1; letter-spacing: -0.005em; }
  .holder__role { font-size: 21px; font-weight: 400; color: var(--brand-red); margin-top: 8px; line-height: 1; }

  .contact-rail { position: absolute; left: 0; top: 222px; width: 72px; height: 257px; background: var(--brand-blue); border-radius: 0 5px 0 0; }
  .contact-rail svg { position: absolute; left: 33px; transform: translateX(-50%); }
  .contact-list { position: absolute; left: 87px; top: 248px; list-style: none; }
  .contact-list li { font-size: 18px; line-height: 1; padding-bottom: 7px; border-bottom: 1px solid var(--line-red); margin-bottom: 22px; }
</style>
</head>
<body>
<div class="stage">
  <div class="card-shadow" style="left:203px; top:132px; width:838px; height:479px;"></div>
  <div class="card-shadow" style="left:203px; top:633px; width:838px; height:479px;"></div>

  <section class="card card--front front">
    <svg class="band" style="left:0;top:0" width="838" height="479" aria-hidden="true">
      <polygon points="0,0 457,0 431,23 0,23" fill="var(--brand-red)"/>
      <polygon points="406,455 838,455 838,479 380,479" fill="var(--ink)"/>
    </svg>
    <div class="brand-dot"></div>
    <div class="wordmark">
      <div class="wordmark__name">KEYSTONE</div>
      <div class="wordmark__tagline">Property Partners</div>
      <div class="wordmark__acn">A.C.N 418 902 336</div>
    </div>
  </section>

  <section class="card card--back back">
    <div class="name-tab__stem"></div>
    <div class="name-tab">
      <svg width="28" height="34" viewBox="0 0 28 34" aria-hidden="true">
        <circle cx="14" cy="8" r="8" fill="#fff"/>
        <path d="M1 34 V28 C1 20 7 17 14 17 C21 17 27 20 27 28 V34 Z" fill="#fff"/>
      </svg>
    </div>
    <div class="holder">
      <div class="holder__name">Your Name</div>
      <div class="holder__role">Your Position</div>
    </div>

    <div class="contact-rail">
      <svg style="top:29px" width="26" height="19" viewBox="0 0 26 19" aria-hidden="true">
        <rect x="0" y="0" width="26" height="19" rx="3" fill="#fff"/>
        <path d="M3 4 L13 12 L23 4 M3 16 L9 10 M23 16 L17 10" stroke="var(--brand-blue)" stroke-width="1.6" fill="none"/>
      </svg>
      <svg style="top:74px" width="26" height="26" viewBox="0 0 26 26" aria-hidden="true">
        <circle cx="13" cy="13" r="12" fill="#fff"/>
        <path d="M1 13 H25 M13 1 V25 M3 7 H23 M3 19 H23 M13 1 C7 7 7 19 13 25 M13 1 C19 7 19 19 13 25" stroke="var(--brand-blue)" stroke-width="1.5" fill="none"/>
      </svg>
      <svg style="top:123px" width="24" height="24" viewBox="0 0 24 24" aria-hidden="true">
        <path d="M5 2 L9 6 L7 9 C8 12 11 15 14 16 L17 14 L21 18 L18 22 C10 21 3 14 2 6 Z" fill="#fff"/>
        <path d="M14 3 A7 7 0 0 1 21 10 M14 7 A3 3 0 0 1 17 10" stroke="#fff" stroke-width="1.8" fill="none"/>
      </svg>
      <svg style="top:172px" width="22" height="28" viewBox="0 0 22 28" aria-hidden="true">
        <path d="M11 28 C4 19 0 14 0 10 A11 11 0 0 1 22 10 C22 14 18 19 11 28 Z" fill="#fff"/>
        <circle cx="11" cy="10" r="4" fill="var(--brand-blue)"/>
      </svg>
    </div>
    <ul class="contact-list">
      <li style="width:218px">Youremail@mailbox.com</li>
      <li style="width:208px">www.yourwebsite.com</li>
      <li style="width:288px">+99999 99999,&nbsp; +88888 88888</li>
      <li style="width:224px">Your Company Address.</li>
    </ul>

    <svg class="band" style="left:0;top:0" width="838" height="479" aria-hidden="true">
      <polygon points="401,452 838,452 838,479 362,479" fill="var(--ink)"/>
    </svg>
    <div class="brand-dot"></div>
    <div class="wordmark">
      <div class="wordmark__name">KEYSTONE</div>
      <div class="wordmark__tagline">Property Partners</div>
      <div class="wordmark__acn">A.C.N 418 902 336</div>
    </div>
  </section>
</div>
</body>
</html>
```